Healthcare website - Diabetic Shoes - Elderfund - No Cost

I am looking to upgrade my website. I do not want to use Wordpress, Adobe Muse or another designing program. The code should be easily editable using textpad or VI. After the project is done I want to easily add my custom PHP code.

Features
Creative and Modern Design .
Fully responsive site for use on mobile devices
bootstrap, jquery

My current website is
www.pebblewalkco.com

Target Market(s)

Older people who have diabetes. Target market is +60 years old, but we do have younger people going to the site to help out their parents.

Industry/Entity Type

Healthcare

Coding

Coded - Design and coding required

Number of Pages Required

2 page

Colors

Designer to choose colors to be used in the design.

Requirements
Must have
• The code should be easily editable using textpad or VI. After the project is done I want to easily add my custom PHP code.
• The first page will be the home page and the other page I need is this form.
• https://www.pebblewalkco.com/pebble-walk-co-do-i-qualify.php
Should not have
• I do not want to use Wordpress, Adobe Muse or another designing program.

```html
<!DOCTYPE html>
<html lang="en">
<head>
<meta charset="utf-8">
<title>Pebble Walk Co — Diabetic Shoes Covered by Elderfund</title>
<link href="https://fonts.googleapis.com/css2?family=Open+Sans:wght@400;600;700&display=swap" rel="stylesheet">
<style>
:root{
  --green:#5fb548;
  --green-dark:#4e9e3a;
  --blue:#3f74a6;
  --blue-deep:#355f8c;
  --navy:#2f4f6f;
  --ink:#333b44;
  --muted:#6b7580;
  --line:#d9dde2;
  --soft:#f3f4f6;
  --white:#ffffff;
}
*{box-sizing:border-box;margin:0;padding:0}
html,body{width:1200px;height:4036px;overflow:hidden}
body{font-family:"Open Sans",Arial,sans-serif;color:var(--ink);background:var(--white);position:relative}
section,header,footer{position:relative;width:1200px}
.section-title{position:absolute;left:0;width:1200px;text-align:center;color:var(--green);font-weight:700;font-size:30px;letter-spacing:.5px}
.section-title::after{content:"";display:block;width:70px;height:2px;background:var(--green);margin:12px auto 0}
.btn{display:inline-block;background:var(--navy);color:var(--white);font-weight:600;text-transform:uppercase;font-size:15px;text-align:center}

/* header */
.site-header{height:135px}
.brand{position:absolute;left:100px;top:34px}
.brand-name{font-size:44px;font-weight:600;color:var(--green);line-height:1}
.brand-sub{font-size:16px;font-style:italic;color:var(--navy);margin-top:6px}
.phone{position:absolute;left:688px;top:26px;display:flex;align-items:center;gap:8px;font-size:33px;color:var(--ink)}
.login{position:absolute;left:1003px;top:27px;width:97px;height:34px;background:var(--green);color:#fff;font-size:15px;line-height:34px;text-align:center}
.main-nav{position:absolute;right:100px;top:92px;font-size:13px;text-transform:uppercase;color:var(--navy);display:flex;gap:10px}
.main-nav span.sep{color:var(--line)}
.main-nav .active{color:var(--green)}

/* hero */
.hero{height:597px;overflow:hidden}
.hero-photo{position:absolute;inset:0;background:linear-gradient(180deg,#8e8a86 0%,#a98c6e 45%,#b98e62 75%,#c59b6b 100%)}
.hero-shade{position:absolute;inset:0;background:rgba(0,0,0,.18)}
.hero h1{position:absolute;top:180px;width:1200px;text-align:center;color:#fff;font-size:37px;font-weight:600;text-transform:uppercase;letter-spacing:.5px}
.hero p{position:absolute;top:236px;left:100px;width:1000px;text-align:center;color:#fff;font-size:15px;line-height:25px}
.dots{position:absolute;top:502px;width:1200px;display:flex;justify-content:center;gap:6px}
.dots i{width:16px;height:16px;border-radius:50%;background:#fff;display:block}
.dots i.on{background:transparent;border:2px solid #fff}
.hero-curve{position:absolute;bottom:0;left:0}

/* about */
.about{height:452px}
.about .section-title{top:28px}
.about-text{position:absolute;left:100px;top:120px;width:545px;font-size:14px;line-height:24px;color:var(--ink)}
.about .btn{position:absolute;left:100px;top:312px;width:258px;height:44px;line-height:44px}
.about-photo{position:absolute;left:720px;top:62px;width:380px;height:248px;border:1px solid var(--line);padding:10px;background:#fff;box-shadow:0 1px 3px rgba(0,0,0,.08)}
.about-photo div{width:100%;height:100%;background:linear-gradient(160deg,#f5f2ee 0%,#e8dfd4 50%,#cdb8a2 100%)}

/* steps */
.steps{height:444px;background:var(--soft)}
.steps .section-title{top:78px;font-size:28px}
.steps .section-title::after{display:none}
.step-row{position:absolute;top:156px;left:0;width:1200px;height:200px}
.step-icon{position:absolute;top:0;width:120px;height:120px;border-radius:50%;background:var(--blue);border:5px solid #fff;box-shadow:0 0 0 2px #b8c9dc}
.step-text{position:absolute;top:138px;width:200px;text-align:center;font-size:14px;line-height:20px;color:var(--ink)}
.arrow{position:absolute;top:52px}

/* philosophy */
.philosophy{height:438px;background:var(--blue);color:#fff}
.philosophy h2{position:absolute;top:58px;width:1200px;text-align:center;font-size:30px;font-weight:400;letter-spacing:1px}
.philosophy h2::after{content:"";display:block;width:70px;height:2px;background:#fff;margin:12px auto 0}
.philosophy .copy{position:absolute;top:145px;left:100px;width:1000px;text-align:center;font-size:13.5px;line-height:24px}
.philosophy .copy p+p{margin-top:22px}

/* video */
.video{height:436px}
.video .section-title{top:60px}
.video-text{position:absolute;left:100px;top:130px;width:520px}
.video-text h3{font-size:18px;font-weight:400;color:var(--ink);margin-bottom:8px}
.video-text p{font-size:12.5px;line-height:21px;color:var(--muted);margin-bottom:12px}
.video .btn{position:absolute;left:100px;top:335px;width:230px;height:46px;line-height:46px;background:var(--blue-deep);font-weight:400;font-size:17px}
.player{position:absolute;left:667px;top:129px;width:433px;height:285px;border:1px solid var(--line);background:#fff}
.player-frame{position:absolute;left:10px;top:10px;right:10px;bottom:36px;background:linear-gradient(180deg,#ffffff,#eef1f4)}
.player-bar{position:absolute;left:10px;right:10px;bottom:10px;height:26px;background:#1e1e1e}

/* products */
.products{height:713px;background:var(--soft)}
.products .section-title{top:48px}
.card{position:absolute;top:220px;width:234px}
.card-photo{width:234px;height:223px;background:#fff;border:1px solid var(--line);box-shadow:0 1px 4px rgba(0,0,0,.12);padding:14px}
.card-photo div{width:100%;height:100%;background:radial-gradient(ellipse at center,#cfd3d8 0%,#f4f5f6 55%,#fff 75%)}
.card h4{text-align:center;font-size:14px;font-weight:700;margin-top:30px;text-transform:uppercase}
.card p{text-align:center;font-size:12.5px;line-height:20px;color:var(--muted);margin-top:10px;padding:0 18px}
.card .btn{display:block;margin:14px auto 0;width:114px;height:38px;line-height:38px;font-size:13px;background:var(--blue-deep)}

/* catalog */
.catalog{height:475px}
.catalog .section-title{top:72px}
.field{position:absolute;height:44px;border:1px solid var(--line);font-size:12px;color:#9aa2ab;padding:13px 12px}
.catalog .submit{position:absolute;left:495px;top:349px;width:210px;height:50px;border:2px solid var(--line);color:var(--navy);font-size:17px;line-height:46px;text-align:center;text-transform:uppercase}

/* footer */
.site-footer{height:346px;background:var(--blue);color:#fff}
.site-footer h5{font-size:16px;font-weight:600;text-transform:uppercase;margin-bottom:18px}
.col{position:absolute;top:55px}
.col ul{list-style:none;font-size:13.5px;line-height:27px}
.contact-line{font-size:13.5px;line-height:27px}
.subscribe{display:flex;margin-top:14px}
.subscribe span{width:230px;height:40px;background:#fff;color:#9aa2ab;font-size:12px;line-height:40px;padding-left:12px;text-transform:uppercase}
.subscribe b{width:95px;height:40px;background:var(--green);font-size:13px;line-height:40px;text-align:center}
.socials{display:flex;gap:10px;margin-top:18px}
.socials i{display:block;width:38px;height:38px;border-radius:50%;background:#fff}
.footer-rule{position:absolute;left:0;top:291px;width:1200px;height:1px;background:rgba(255,255,255,.35)}
.copyright{position:absolute;left:100px;top:312px;font-size:12.5px}
</style>
</head>
<body>

<header class="site-header">
  <div class="brand">
    <div class="brand-name">Pebble Walk Co</div>
    <div class="brand-sub">By Meridian Care Supply</div>
  </div>
  <div class="phone">
    <svg width="38" height="38" viewBox="0 0 40 40" aria-hidden="true"><circle cx="20" cy="20" r="17" fill="none" stroke="#333b44" stroke-width="3"/><path d="M13 11c1-1 3-1 4 0l2 3c1 1 0 2-1 3 1 2 3 4 5 5 1-1 2-2 3-1l3 2c1 1 1 3 0 4-2 2-5 2-8 0-4-3-7-6-9-10-1-3-1-5 1-6z" fill="#333b44"/></svg>
    <span>1-800-555-0142</span>
  </div>
  <div class="login">Login</div>
  <nav class="main-nav">
    <span class="active">Home</span><span class="sep">|</span>
    <span>Pebble Walk Co/ Do I Qualify?</span><span class="sep">|</span>
    <span>Why Diabetic Shoes?</span><span class="sep">|</span>
    <span>Shoes</span><span class="sep">|</span>
    <span>Products</span><span class="sep">|</span>
    <span>Shoe Fitter Jobs</span><span class="sep">|</span>
    <span>FAQ</span>
  </nav>
</header>

<section class="hero">
  <div class="hero-photo" role="img" aria-label="Pairs of diabetic sneakers and dress shoes with orthotic insoles on a wooden floor beside bare feet"></div>
  <div class="hero-shade"></div>
  <h1>Diabetic Shoes or Sneakers Covered by Elderfund</h1>
  <p>No or little out of pocket Cost To You!* Elderfund, and most insurance plans, may cover the cost of one pair of diabetic shoes and three pairs<br>of custom inserts per calendar year. Co-payments, deductibles and some restrictions apply.</p>
  <div class="dots"><i></i><i class="on"></i><i></i><i></i></div>
  <svg class="hero-curve" width="1200" height="60" viewBox="0 0 1200 60" aria-hidden="true"><path d="M0 0 Q600 80 1200 0 L1200 60 L0 60Z" fill="#fff"/></svg>
</section>

<section class="about">
  <h2 class="section-title">ABOUT US</h2>
  <p class="about-text">Pebble Walk Co was created by Meridian Care Supply to educate clients and prospective shoe fitters about diabetic shoes and the coverage that Elderfund provides. Founded by a Board-Certified Pedorthist, the company’s mission is to help clients receive properly fitted shoes from qualified healthcare professionals around the United States. Meridian Care Supply works directly with Elderfund to determine the patient’s coverage.</p>
  <span class="btn">Read More Information</span>
  <div class="about-photo"><div role="img" aria-label="Close-up of a walking shoe stepping forward on a path"></div></div>
</section>

<section class="steps">
  <h2 class="section-title">4 Easy Steps To Receive Your New Therapeutic Shoes.</h2>
  <div class="step-row">
    <div class="step-icon" style="left:155px">
      <svg width="110" height="110" viewBox="0 0 110 110" aria-hidden="true"><rect x="38" y="34" width="30" height="38" rx="2" fill="none" stroke="#fff" stroke-width="3"/><path d="M44 44h18M44 52h18M44 60h10" stroke="#fff" stroke-width="3"/><path d="M62 66l12-14 4 4-12 14-6 2z" fill="#fff"/></svg>
    </div>
    <div class="step-icon" style="left:410px">
      <svg width="110" height="110" viewBox="0 0 110 110" aria-hidden="true"><circle cx="55" cy="42" r="11" fill="#fff"/><path d="M33 76c2-14 10-20 22-20s20 6 22 20z" fill="#fff"/><path d="M52 60h6l-1 12h-4z" fill="#3f74a6"/></svg>
    </div>
    <div class="step-icon" style="left:666px">
      <svg width="110" height="110" viewBox="0 0 110 110" aria-hidden="true"><path d="M30 66c0-6 4-10 8-14l8-10c3 6 10 8 16 6l12 10c4 2 8 4 8 8v4H30z" fill="#fff"/></svg>
    </div>
    <div class="step-icon" style="left:922px">
      <svg width="110" height="110" viewBox="0 0 110 110" aria-hidden="true"><rect x="34" y="50" width="10" height="24" fill="#fff"/><path d="M48 50l10-16c3-4 7-2 6 3l-3 9h14c4 0 6 3 5 6l-4 18c-1 3-3 4-6 4H48z" fill="#fff"/></svg>
    </div>
    <svg class="arrow" style="left:285px" width="120" height="20" viewBox="0 0 120 20" aria-hidden="true"><path d="M0 10h110" stroke="#3f74a6" stroke-width="3"/><path d="M108 3l10 7-10 7z" fill="#3f74a6"/></svg>
    <svg class="arrow" style="left:540px" width="120" height="20" viewBox="0 0 120 20" aria-hidden="true"><path d="M0 10h110" stroke="#3f74a6" stroke-width="3"/><path d="M108 3l10 7-10 7z" fill="#3f74a6"/></svg>
    <svg class="arrow" style="left:796px" width="120" height="20" viewBox="0 0 120 20" aria-hidden="true"><path d="M0 10h110" stroke="#3f74a6" stroke-width="3"/><path d="M108 3l10 7-10 7z" fill="#3f74a6"/></svg>
    <p class="step-text" style="left:115px">Fill out an application to see if you qualify.</p>
    <p class="step-text" style="left:370px">A prescription will be faxed to your primary physician.</p>
    <p class="step-text" style="left:626px">After the prescription is signed, a certified shoe fitter will fit your new shoes.</p>
    <p class="step-text" style="left:882px">Enjoy your new shoes!</p>
  </div>
</section>

<section class="philosophy">
  <h2>OUR PHILOSOPHY</h2>
  <div class="copy">
    <p>At Meridian Care Supply, we understand the health benefits and medical safety associated with properly fitted shoes. We strive to educate clients about wearing appropriate footwear and avoiding unnecessary complications. One in four Americans with diabetes will develop potentially serious foot problems related to the disease. By educating our clients and connecting them with leading healthcare professionals, we keep diabetic patients on their feet and mobile. PebbleWalkCo.com further benefits clients by preventing future expenses that result from ill-fitting shoes.</p>
    <p>Meridian Care Supply connects patients, podiatrists, certified shoe fitters, pedorthists, and providers through its accessible database system. Meridian Care Supply works with Elderfund directly and helps patients find diabetic shoes and a conveniently located shoe fitter in their area.</p>
  </div>
</section>

<section class="video">
  <h2 class="section-title">OUR VIDEO</h2>
  <div class="video-text">
    <h3>How Does Diabetes Cause Foot Problems?</h3>
    <p>Diabetes can cause neuropathy (nerve damage), which reduces feeling in your feet. This makes you less likely to feel the early warning signs of foot problems. Decreased circulation reduces the ability to heal and fight off infection. These two conditions significantly increase the likelihood of foot complications, infection, and ulceration.</p>
    <h3>Why Are Properly Fitted Shoes Important?</h3>
    <p>Twenty four million people have diabetes, and twenty-five percent of this population will develop foot problems caused by their disease.</p>
  </div>
  <span class="btn">More Information &nbsp;›</span>
  <div class="player">
    <div class="player-frame" role="img" aria-label="Video still inviting viewers to sign up online or by phone, with a play button"></div>
    <div class="player-bar"></div>
  </div>
</section>

<section class="products">
  <h2 class="section-title">OUR ELDERFUND PRODUCTS</h2>
  <div class="card" style="left:100px">
    <div class="card-photo"><div role="img" aria-label="Black and red diabetic sneaker"></div></div>
    <h4>Strideline - SL408-Black-Red</h4>
    <p>Our orthopedic shoes reduce the pressure and friction on your feet that can lead to foot injuries</p>
    <span class="btn">Read More</span>
  </div>
  <div class="card" style="left:355px">
    <div class="card-photo"><div role="img" aria-label="Navy and blue diabetic sneaker"></div></div>
    <h4>Strideline - SL408-Black-Red</h4>
    <p>Our orthopedic shoes reduce the pressure and friction on your feet that can lead to foot injuries</p>
    <span class="btn">Read More</span>
  </div>
  <div class="card" style="left:611px">
    <div class="card-photo"><div role="img" aria-label="Grey diabetic sneaker"></div></div>
    <h4>Strideline - SL408-Black-Red</h4>
    <p>Our orthopedic shoes reduce the pressure and friction on your feet that can lead to foot injuries</p>
    <span class="btn">Read More</span>
  </div>
  <div class="card" style="left:866px">
    <div class="card-photo"><div role="img" aria-label="Black knee, ankle and wrist braces"></div></div>
    <h4>Knee, Ankle, Wrist Braces</h4>
    <p>Our knees are susceptible to injuries because they support the entire weight of our bodies.</p>
    <span class="btn">Read More</span>
  </div>
</section>

<section class="catalog">
  <h2 class="section-title" style="font-size:29px">REQUEST A FREE DIABETIC SHOE CATALOG</h2>
  <div class="field" style="left:100px;top:166px;width:237px">First name</div>
  <div class="field" style="left:355px;top:166px;width:237px">Last name</div>
  <div class="field" style="left:609px;top:166px;width:237px">Email address</div>
  <div class="field" style="left:863px;top:166px;width:237px">Phone number</div>
  <div class="field" style="left:100px;top:234px;width:1000px;height:68px">Message</div>
  <div class="submit">Request Catalog</div>
</section>

<footer class="site-footer">
  <div class="col" style="left:100px">
    <h5>Quick Links</h5>
    <div style="display:flex;gap:72px">
      <ul><li>Home</li><li>About Us</li><li>Video</li><li>Products</li><li>Contact</li></ul>
      <ul><li>Terms of Use</li><li>Privacy Policy</li><li>Returns/Exchanges</li><li>FAQS</li></ul>
    </div>
  </div>
  <div class="col" style="left:470px">
    <h5>Contact Info</h5>
    <p class="contact-line">Pebble Walk Co, Street No, City Name,<br>Country Name, Code</p>
    <p class="contact-line">
      <svg width="14" height="14" viewBox="0 0 14 14" aria-hidden="true"><path d="M3 1l2 3-1 2c1 2 2 3 4 4l2-1 3 2-1 2C6 13 1 8 1 2z" fill="#fff"/></svg>
      &nbsp;1-800-555-0142</p>
    <p class="contact-line">
      <svg width="14" height="11" viewBox="0 0 14 11" aria-hidden="true"><rect width="14" height="11" fill="#fff"/><path d="M0 0l7 6 7-6" fill="none" stroke="#3f74a6" stroke-width="1.5"/></svg>
      &nbsp;info@pebblewalkco.com</p>
  </div>
  <div class="col" style="left:775px">
    <h5>Sign Up for Newsletters</h5>
    <p style="font-size:13.5px">Please sign up here for latest news</p>
    <div class="subscribe"><span>Email address</span><b>SUBSCRIBE</b></div>
    <div class="socials"><i></i><i></i><i></i><i></i></div>
  </div>
  <div class="footer-rule"></div>
  <p class="copyright">© 2017 PEBBLE WALK CO. All right reserved . Term of Use</p>
</footer>

</body>
</html>
```